Business card design needed

I need a business card for my new business.
I make environmentally friendly candles from all natural premium ingredients.
The candles are hand-poured locally in Melbourne, Australia.
I also want my card to match my website www.velmoracandles-example.com.au (similar colours, font). Can add additional fonts to create more interest...
I want my design to reflect class and simplicity.
Target Market(s)
Target audience 25-50
The candles represent luxury but need to appeal to the environmentally conscious...
Needs to appeal to both men and women. A luxury gift a man would buy for his girlfriend or mother or for his home and for a woman it needs to represent quality...
Industry/Entity Type
Business
Contact Information for Business Card
Velmora Candles
Hand-Poured Eco Soy Candles
Lorena Whitcombe - Founder
0472 390 614
www.velmoracandles-example.com.au
Logo Text
VELMORA
Logo styles of interest
Wordmark Logo
Look and feel
Each slider illustrates characteristics of the customer's brand and the style your logo design should communicate.

```html
<!DOCTYPE html>
<html lang="en">
<head>
<meta charset="utf-8">
<title>Velmora Candles – Business Card</title>
<link href="https://fonts.googleapis.com/css2?family=Roboto+Slab:wght@300;400&display=swap" rel="stylesheet">
<style>
  :root {
    --backdrop: #ededed;
    --card-white: #fbfbfb;
    --slate: #7a7a7a;
    --ink: #6a6a6a;
    --ink-soft: #8a8a8a;
    --aqua: #b6e3e1;
    --paper-text: #f4f4f4;
  }
  * { box-sizing: border-box; margin: 0; padding: 0; }
  html, body {
    width: 1200px; height: 910px; overflow: hidden;
    background: var(--backdrop);
    font-family: "Roboto Slab", Georgia, serif;
  }
  .canvas { position: relative; width: 1200px; height: 910px; }

  .card {
    position: absolute;
    width: 640px; height: 391px;
    box-shadow: 0 10px 24px rgba(0,0,0,0.12);
    overflow: hidden;
  }
  .card--back { left: 480px; top: 48px; background: var(--slate); }
  .card--front { left: 80px; top: 470px; background: var(--card-white); }

  .brand {
    position: absolute; left: 0; right: 0;
    text-align: center;
  }
  .card--back .brand { top: 150px; color: var(--paper-text); }
  .card--front .brand { top: 54px; color: var(--ink); }

  .brand__name {
    font-weight: 400; font-size: 40px; letter-spacing: 1px; line-height: 1.1;
  }
  .brand__tagline {
    margin-top: 10px;
    font-size: 14px; font-weight: 400; letter-spacing: 0.4px;
  }

  .holder {
    position: absolute; left: 0; right: 0; top: 176px;
    text-align: center; color: var(--ink);
  }
  .holder__name { font-size: 20px; font-weight: 400; letter-spacing: 1px; }
  .holder__role { font-size: 13px; color: var(--ink-soft); margin-top: 4px; }

  .contact-band {
    position: absolute; left: 0; right: 0; bottom: 0; height: 92px;
    background: var(--slate);
    border-top: 5px solid var(--aqua);
    display: flex; align-items: center; gap: 38px;
    padding-left: 36px;
  }
  .contact {
    display: flex; align-items: center; gap: 10px;
    color: var(--paper-text); font-size: 15px; font-weight: 300; letter-spacing: 0.3px;
    white-space: nowrap;
  }
  .contact svg { width: 22px; height: 22px; flex: none; }
</style>
</head>
<body>
<main class="canvas">

  <section class="card card--back" aria-label="Business card back">
    <div class="brand">
      <div class="brand__name">VELMORA CANDLES</div>
      <div class="brand__tagline">Hand-Poured Eco Soy Candles</div>
    </div>
  </section>

  <section class="card card--front" aria-label="Business card front">
    <div class="brand">
      <div class="brand__name">VELMORA CANDLES</div>
      <div class="brand__tagline">Hand-Poured Eco Soy Candles</div>
    </div>

    <div class="holder">
      <div class="holder__name">LORENA WHITCOMBE</div>
      <div class="holder__role">Founder</div>
    </div>

    <div class="contact-band">
      <div class="contact">
        <svg viewBox="0 0 24 24" aria-hidden="true">
          <circle cx="12" cy="12" r="10.5" fill="none" stroke="#b6e3e1" stroke-width="1.3"/>
          <path d="M9 6.5c-.8 0-1.6 1-1.6 2 0 3.8 3.6 8 7.6 8.6 1 .1 2-.7 2.1-1.5l-2-1.6-1.3.9c-1.6-.7-3-2.3-3.5-3.9l.9-1.3L9.7 6.7z" fill="#b6e3e1"/>
        </svg>
        <span>0472 390 614</span>
      </div>
      <div class="contact">
        <svg viewBox="0 0 24 24" aria-hidden="true">
          <circle cx="12" cy="12" r="10.5" fill="none" stroke="#b6e3e1" stroke-width="1.3"/>
          <g fill="none" stroke="#b6e3e1" stroke-width="1.1">
            <circle cx="12" cy="12" r="6.5"/>
            <ellipse cx="12" cy="12" rx="3" ry="6.5"/>
            <line x1="5.5" y1="12" x2="18.5" y2="12"/>
            <line x1="6.5" y1="9" x2="17.5" y2="9"/>
            <line x1="6.5" y1="15" x2="17.5" y2="15"/>
          </g>
        </svg>
        <span>www.velmoracandles-example.com.au</span>
      </div>
    </div>
  </section>

</main>
</body>
</html>
```